Business card design needed

I have a leadership coaching and consultancy business which specialises in the education sector. I would like a clean, professional design). The design needs to speak to strength, support, new learning, connections & a growth mindest.

I am also looking for a unique LOGO. This is very important.

Target Market(s)

Educational Leaders & executives

Industry/Entity Type

Leadership

Contact Information for Business Card

Miranda Voss
Principal Coach & Consultant
Miranda Voss Coaching & Consulting
0491 362 815
miranda.voss@quillmail.example
I also would like my facebook, twitter and linkedin accounts to appear

Logo styles of interest
Lettermark Logo
Requirements
Must have
• A 2 sided business card with contact details on the back
A logo

```html
<!DOCTYPE html>
<html lang="en">
<head>
<meta charset="utf-8">
<title>Miranda Voss — Business Card Front</title>
<link rel="stylesheet" href="https://fonts.googleapis.com/css2?family=Oswald:wght@400;500&display=swap">
<style>
  :root {
    --card-yellow: #ffcd08;
    --band-white: #ffffff;
    --ink: #231f20;
    --title-grey: #7b7b7b;
    --shadow: #3a2e00;
  }
  html, body {
    margin: 0;
    padding: 0;
    width: 1200px;
    height: 693px;
    overflow: hidden;
    background: var(--card-yellow);
  }
  .card-front {
    display: block;
    width: 1200px;
    height: 693px;
  }
  .card-background { fill: var(--card-yellow); }
  .fold-shadow { fill: var(--shadow); }
  .name-band { fill: var(--band-white); }
  .holder-name {
    font-family: "Oswald", "Arial Narrow", sans-serif;
    font-weight: 500;
    font-size: 100px;
    fill: var(--ink);
    letter-spacing: 1px;
  }
  .holder-title {
    font-family: "Oswald", "Arial Narrow", sans-serif;
    font-weight: 400;
    font-size: 55px;
    fill: var(--title-grey);
  }
</style>
</head>
<body>
<svg class="card-front" viewBox="0 0 1200 693" xmlns="http://www.w3.org/2000/svg" aria-label="Miranda Voss, Principal Coach and Consultant">
  <defs>
    <filter id="soft-blur" x="-50%" y="-50%" width="200%" height="200%">
      <feGaussianBlur stdDeviation="6"/>
    </filter>
    <filter id="wide-blur" x="-50%" y="-50%" width="200%" height="200%">
      <feGaussianBlur stdDeviation="9"/>
    </filter>
    <linearGradient id="band-curl" x1="0" y1="0" x2="1" y2="0">
      <stop offset="0" stop-color="#b9b9b9"/>
      <stop offset="0.35" stop-color="#e4e4e4"/>
      <stop offset="1" stop-color="#ffffff"/>
    </linearGradient>
    <linearGradient id="slot-fade" x1="0" y1="0" x2="0" y2="1">
      <stop offset="0" stop-color="#000" stop-opacity="0"/>
      <stop offset="0.25" stop-color="#000" stop-opacity="0.55"/>
      <stop offset="0.75" stop-color="#000" stop-opacity="0.55"/>
      <stop offset="1" stop-color="#000" stop-opacity="0"/>
    </linearGradient>
  </defs>

  <rect class="card-background" width="1200" height="693"/>

  <!-- slot shadow where the band tucks in -->
  <rect x="124" y="70" width="10" height="520" fill="url(#slot-fade)" filter="url(#soft-blur)"/>

  <!-- lift shadow under the band's right end -->
  <path class="fold-shadow" d="M880 468 L1062 472 Q1055 490 1040 497 Z" opacity="0.75" filter="url(#wide-blur)"/>

  <!-- the white name band -->
  <rect class="name-band" x="125" y="194" width="950" height="277" rx="2"/>
  <rect x="125" y="194" width="30" height="277" fill="url(#band-curl)"/>

  <text class="holder-name" x="262" y="330">MIRANDA VOSS</text>
  <text class="holder-title" x="359" y="412" textLength="569" lengthAdjust="spacingAndGlyphs">PRINCIPAL COACH &amp; CONSULTANT</text>
</svg>
</body>
</html>
```